Create a Branded Excel Invoice for a Jewellery Company

Hi,

I need an invoice template created for a jewelry company. The invoice must have a color scheme that matches the logo. I attached a sample invoice below, this is only for REFERENCE so that you know what fields should be in the invoice.

For all the fields refer to the sample invoice I attached. The content should be the same but the actual color and layout can be different.

-Color must match the logo
-Must have branding
-Must be a consistent color scheme
-Must have all the fields as in the invoice example
-Use placeholder text until awarded entry
-Must be in EXCEL format

I will rate all the entries, please stay away from ideas that get less than 3 stars.

```html
<!DOCTYPE html>
<html lang="en">
<head>
<meta charset="UTF-8">
<title>Invoice 1230 – Corra Jewellery</title>
<link rel="stylesheet" href="https://fonts.googleapis.com/css2?family=Cinzel:wght@400&family=Carlito:wght@400;700&family=PT+Sans:wght@400&display=swap">
<style>
  :root {
    --gold: #c9a46e;
    --gold-line: #d6b88a;
    --ink: #1f1f1f;
    --paper: #ffffff;
  }
  html, body {
    margin: 0;
    padding: 0;
    overflow: hidden;
    background: var(--paper);
  }
  .invoice {
    position: relative;
    width: 1192px;
    height: 1200px;
    overflow: hidden;
    background: var(--paper);
    color: var(--ink);
    font-family: "PT Sans", sans-serif;
    font-size: 20px;
  }
  .invoice * { box-sizing: border-box; }

  .brand-name {
    position: absolute;
    left: 84px;
    top: 180px;
    width: 400px;
    margin: 0;
    font-family: "PT Sans", sans-serif;
    font-weight: 400;
    font-size: 38px;
    line-height: 48px;
    white-space: nowrap;
    color: var(--gold);
    text-align: center;
  }

  .info-block {
    position: absolute;
    display: grid;
    margin: 0;
  }
  .info-block dt, .info-block dd {
    margin: 0;
    line-height: 33px;
    white-space: nowrap;
  }
  .info-block dt {
    font-family: "Carlito", sans-serif;
    color: var(--gold);
    font-size: 21px;
  }
  .info-block dd {
    border-left: 1px solid var(--gold-line);
    padding-left: 22px;
  }
  .invoice-meta {
    left: 607px;
    top: 138px;
    grid-template-columns: 156px auto;
  }

  .rule {
    position: absolute;
    left: 60px;
    width: 1071px;
    height: 2px;
    background: var(--gold-line);
  }
  .rule--top { top: 334px; }
  .rule--bottom { top: 431px; }

  .doc-title {
    position: absolute;
    left: 60px;
    top: 354px;
    width: 1071px;
    margin: 0;
    text-align: center;
    font-family: "Cinzel", serif;
    font-weight: 400;
    font-size: 48px;
    line-height: 60px;
    color: var(--gold);
  }

  .party {
    position: absolute;
    top: 479px;
    display: flex;
  }
  .party__label {
    font-family: "Carlito", sans-serif;
    color: var(--gold);
    font-size: 21px;
    line-height: 33px;
  }
  .party__address {
    font-style: normal;
    border-left: 1px solid var(--gold-line);
    padding-left: 22px;
    line-height: 33px;
  }
  .party--from { left: 107px; }
  .party--from .party__label { width: 93px; }
  .party--for { left: 668px; }
  .party--for .party__label { width: 95px; }

  .line-items {
    position: absolute;
    left: 60px;
    top: 708px;
    width: 1073px;
    border-collapse: collapse;
  }
  .line-items th {
    font-family: "Carlito", sans-serif;
    font-weight: 400;
    color: var(--gold);
    font-size: 21px;
    height: 34px;
    text-align: left;
    border-bottom: 1px solid var(--gold-line);
    padding: 0;
  }
  .line-items td {
    height: 50px;
    padding: 0 0 4px;
    vertical-align: bottom;
  }
  .line-items tbody tr:first-child td { height: 54px; }
  .line-items tbody tr:last-child td { border-bottom: 1px solid var(--gold-line); padding-bottom: 6px; }
  .line-items .col-type { width: 141px; padding-left: 5px; }
  .line-items .num { text-align: right; }
  .col-unit { width: 167px; }
  .col-amount { width: 207px; }

  .totals {
    position: absolute;
    right: 59px;
    top: 926px;
    display: grid;
    grid-template-columns: auto 210px;
    margin: 0;
    font-family: "Carlito", sans-serif;
    font-size: 21px;
  }
  .totals dt, .totals dd {
    margin: 0;
    line-height: 33px;
    text-align: right;
  }
  .totals dt { font-weight: 700; }
  .totals dd { font-family: "PT Sans", sans-serif; font-size: 20px; }

  .amount-due {
    position: absolute;
    right: 65px;
    top: 1061px;
    display: flex;
    gap: 46px;
    font-family: "Carlito", sans-serif;
    font-size: 28px;
    line-height: 38px;
  }
</style>
</head>
<body>
<main class="invoice">
  <header>
    <p class="brand-name">Corra Jewellery</p>
    <dl class="info-block invoice-meta">
      <dt>Invoice ID</dt><dd>1230</dd>
      <dt>Issue Date</dt><dd>22/04/2019</dd>
      <dt>Due Date</dt><dd>26/04/2019 (Upon receipt)</dd>
      <dt>Subject</dt><dd>Spring Marketing Campaign</dd>
    </dl>
  </header>

  <div class="rule rule--top"></div>
  <h1 class="doc-title">INVOICE</h1>
  <div class="rule rule--bottom"></div>

  <section class="party party--from">
    <div class="party__label">From</div>
    <address class="party__address">Lumen Studio<br>28 Harlow Lane<br>Kelbridge KB4 7TR<br>Scotland</address>
  </section>
  <section class="party party--for">
    <div class="party__label">For</div>
    <address class="party__address">Ashcombe Press<br>9 Marlowe Row<br>Dunmere DM2 5QA<br>United Kingdom</address>
  </section>

  <table class="line-items">
    <thead>
      <tr>
        <th class="col-type">Item Type</th>
        <th>Description</th>
        <th class="num">Quantity</th>
        <th class="num col-unit">Unit Price</th>
        <th class="num col-amount">Amount</th>
      </tr>
    </thead>
    <tbody>
      <tr><td class="col-type">Service</td><td>Design</td><td class="num">41.00</td><td class="num">£230.00</td><td class="num">£9,430.00</td></tr>
      <tr><td class="col-type">Service</td><td>Development</td><td class="num">57.00</td><td class="num">£330.00</td><td class="num">£18,810.00</td></tr>
      <tr><td class="col-type">Service</td><td>Meetings</td><td class="num">4.50</td><td class="num">£60.00</td><td class="num">£270.00</td></tr>
    </tbody>
  </table>

  <dl class="totals">
    <dt>Subtotal</dt><dd>£28,510.00</dd>
    <dt>Tax (10%)</dt><dd>£2,851.00</dd>
    <dt>Payments</dt><dd>£313,661.00</dd>
  </dl>

  <div class="amount-due">
    <span class="amount-due__label">Amount Due</span>
    <span class="amount-due__value">£282,300.00</span>
  </div>
</main>
</body>
</html>
```